"Torvek Industries" needs a creative design

We need a Business card design for a new company based in Australia : Melbourne called "Torvek Industries"

The company will primary be importing Furniture . ie Replica Furniture, Home furniture, Office Furniture, Outdoor Furniture and Entertainment Units

We would like to see the design that use the color Champion Red / Platinum Silver on the Logo .

The final design should communicate " Great quality furniture, Best prices and good customer service"

Also in the Business card please add the following info
- ABN : 52384017265
- Email Address : Torvek.Industires@Mailpoint.com
- WebSite : www.TorvekIndustries.com.au
- FB (facebook icon) : [TorvekIndustries] Like us on Facebook [like hand]
- PH : 0472 916 358

Please refer to attachment for the logo

Sans Serif

eb1f27
1b1b1b
5c5c5c
f5f5f5
f04a50

```html
<!DOCTYPE html>
<html lang="en">
<head>
<meta charset="utf-8">
<title>Torvek Industries – Business Card</title>
<link rel="stylesheet" href="https://fonts.googleapis.com/css2?family=Quicksand:wght@400;500&display=swap">
<style>
  :root {
    --backdrop: #e6e6e6;
    --card: #ffffff;
    --accent-red: #f04a50;
    --silver: #8f8f8f;
    --label-grey: #6e6e6e;
    --card-shadow: rgba(27, 27, 27, 0.12);
  }
  * { box-sizing: border-box; margin: 0; padding: 0; }
  html, body {
    width: 1200px;
    height: 815px;
    overflow: hidden;
  }
  body {
    background: var(--backdrop);
    font-family: "Quicksand", sans-serif;
    position: relative;
  }
  .card {
    position: absolute;
    left: 364px;
    width: 486px;
    height: 312px;
    background: var(--card);
    box-shadow: 0 3px 10px var(--card-shadow);
  }
  .card--front { top: 72px; }
  .card--back  { top: 421px; }

  .brand-square {
    display: block;
    background: var(--accent-red);
  }
  .brand-name {
    font-weight: 400;
    color: var(--silver);
    white-space: nowrap;
    line-height: 1;
  }

  /* Front: stacked brand block */
  .front-brand {
    position: absolute;
    left: 0;
    right: 0;
    top: 78px;
    display: flex;
    flex-direction: column;
    align-items: center;
  }
  .front-brand .brand-square {
    width: 50px;
    height: 50px;
  }
  .front-brand .brand-name {
    margin-top: 56px;
    font-size: 37px;
    letter-spacing: 0.2px;
  }

  /* Back: brand block top-left */
  .back-brand {
    position: absolute;
    left: 46px;
    top: 24px;
    display: flex;
    align-items: center;
    gap: 12px;
  }
  .back-brand .brand-square {
    width: 40px;
    height: 40px;
  }
  .back-brand .brand-name {
    font-size: 19px;
  }

  .contact-list {
    position: absolute;
    left: 0;
    top: 126px;
    display: grid;
    grid-template-columns: 174px auto;
    column-gap: 16px;
    row-gap: 6px;
    font-size: 17px;
    line-height: 21px;
  }
  .contact-label {
    text-align: right;
    color: var(--label-grey);
    position: relative;
    padding-right: 2px;
  }
  .contact-label::after {
    content: ":";
    position: absolute;
    right: -8px;
  }
  .contact-value {
    color: var(--accent-red);
    white-space: nowrap;
  }
</style>
</head>
<body>
  <section class="card card--front" aria-label="Business card front">
    <div class="front-brand">
      <span class="brand-square" aria-hidden="true"></span>
      <span class="brand-name">Torvek Industries</span>
    </div>
  </section>

  <section class="card card--back" aria-label="Business card back">
    <div class="back-brand">
      <span class="brand-square" aria-hidden="true"></span>
      <span class="brand-name">Torvek Industries</span>
    </div>
    <dl class="contact-list">
      <dt class="contact-label">ABN</dt>
      <dd class="contact-value">52384017265</dd>
      <dt class="contact-label">Email Address</dt>
      <dd class="contact-value">Torvek.Industires@Mailpoint.com</dd>
      <dt class="contact-label">WebSite</dt>
      <dd class="contact-value">www.TorvekIndustries.com.au</dd>
      <dt class="contact-label">FB</dt>
      <dd class="contact-value">TorvekIndustries</dd>
      <dt class="contact-label">PH</dt>
      <dd class="contact-value">0472 916 358</dd>
    </dl>
  </section>
</body>
</html>
```